Web Design Project

This is a wordpress project for a newly formed biologics company based in the US with international clientele. We do manufacturing of biologically based raw materials using a state of the art facility....Our logo must be incorporated....logo colors Navy and Gray. It is fine to use some color in web design. The viewer will primarily be industry folk.

Velorast Biologics, LLC is a contract manufacturing organization which produces biologically-based raw materials derived primarily from human plasma. The company services include extraction and purification of plasma components, especially proteins and enzymes. The business focuses on biotherapeutics, diagnostic and veterinary markets worldwide.

5 pages a bad example of first page can be found in attached files.....
use stock photos of labs and clean rooms.
Updates

Project Deadline Extended
Reason: I need a bit more time tonprovide feedback.

Project Deadline Extended
Reason: needed time to evaluate existing options

Target Market(s)

target market Pharmaceutical companies and research universities

Industry/Entity Type

Veterinary

Requirements
Must have
• our logo...we will provide some graphics...

```html
<!DOCTYPE html>
<html lang="en">
<head>
<meta charset="utf-8">
<title>Velorast Biologics — Home</title>
<link rel="stylesheet" href="https://fonts.googleapis.com/css2?family=PT+Sans+Narrow:wght@400;700&display=swap">
<style>
  :root {
    --navy: #0b2c5e;
    --navy-deep: #061a3c;
    --blue: #1f5fae;
    --blue-light: #3f86d1;
    --gray-bar: #a9acb1;
    --gray-soft: #e4e6ea;
    --panel: #f4f5f7;
    --text-navy: #1c3768;
    --rule: #9aa3b3;
    --cyan-line: #5fc3d8;
    --white: #ffffff;
  }
  * { box-sizing: border-box; margin: 0; padding: 0; }
  html, body { width: 1200px; height: 1200px; overflow: hidden; background: #ffffff; }
  body { font-family: "PT Sans Narrow", "Arial Narrow", sans-serif; color: var(--text-navy); }

  .page {
    position: relative; width: 1200px; height: 1200px;
    background: linear-gradient(180deg, #fdfdfe 0%, #e9ebee 60%, #c9ccd2 80%);
  }

  /* Header */
  .site-header {
    position: absolute; left: 0; top: 0; width: 1200px; height: 120px;
    display: flex; align-items: center; justify-content: space-between; padding: 0 36px 0 56px;
    background: linear-gradient(180deg, #ffffff 0%, #e7e8eb 100%);
  }
  .brand { display: flex; align-items: center; gap: 14px; }
  .brand-mark { width: 52px; height: 52px; border-radius: 50%; background: var(--navy); }
  .brand-name { font-size: 30px; font-weight: 700; color: var(--navy); }
  .main-nav { display: flex; gap: 10px; }
  .main-nav a {
    font-size: 25px; color: #fff; text-decoration: none; padding: 6px 12px;
    text-shadow: 0 1px 2px rgba(20,30,50,.75);
  }
  .main-nav a.is-current {
    border: 1px solid #8d929a; border-radius: 5px;
    background: linear-gradient(180deg, #f3f4f6, #b9bdc4);
  }

  /* Hero */
  .hero {
    position: absolute; left: 30px; top: 140px; width: 1140px; height: 260px;
    background: linear-gradient(160deg, var(--navy-deep) 0%, var(--blue) 45%, var(--navy) 100%);
    overflow: hidden;
  }
  .hero-swoosh { position: absolute; inset: 0; }
  .hero-photo { position: absolute; border: 3px solid #eef2f8; box-shadow: 0 4px 10px rgba(0,0,0,.45); }
  .hero-photo--left  { left: 235px; top: 38px; width: 150px; height: 170px; background: linear-gradient(160deg, #c8d6e4, #7f98b2); }
  .hero-photo--main  { left: 388px; top: 14px; width: 330px; height: 220px; background: linear-gradient(160deg, #d9e2ea, #8da6bd); }
  .hero-photo--right { left: 724px; top: 38px; width: 210px; height: 170px; background: linear-gradient(160deg, #cfdbe6, #7c94ad); }
  .hero-pager { position: absolute; left: 508px; top: 228px; display: flex; gap: 8px; }
  .hero-pager span {
    width: 22px; height: 22px; border-radius: 50%; font-size: 15px; line-height: 22px; text-align: center;
    color: #dfe8f5; background: rgba(255,255,255,.12);
  }
  .hero-pager span.is-active { background: #0a1428; color: #fff; }

  /* Welcome bar */
  .section-bar {
    position: absolute; left: 56px; top: 412px; width: 1144px; height: 40px;
    background: linear-gradient(180deg, #bfc2c7, var(--gray-bar));
    border-bottom: 2px solid var(--cyan-line);
    padding-left: 20px; font-size: 31px; font-weight: 700; color: #fff; line-height: 40px;
    text-shadow: 0 1px 2px rgba(0,0,0,.35);
  }

  .intro {
    position: absolute; left: 56px; top: 464px; width: 1070px; height: 160px;
    background: var(--panel); padding: 26px 30px; font-size: 19.5px; line-height: 1.38;
    box-shadow: 0 2px 8px rgba(0,0,0,.12);
  }
  .divider-arrow { display: block; margin-top: 10px; }

  .feature {
    position: absolute; top: 668px; left: 30px; width: 1140px; height: 290px;
  }
  .feature-photo {
    position: absolute; left: 0; top: 0; width: 420px; height: 286px;
    background: linear-gradient(170deg, #e7ecef 0%, #b9c6cf 55%, #7f93a4 100%);
  }
  .feature-text {
    position: absolute; left: 450px; top: 0; width: 640px; height: 240px;
    background: var(--panel); padding: 40px 28px; font-size: 19.5px; line-height: 1.38;
    box-shadow: 0 2px 8px rgba(0,0,0,.12);
  }
  .feature-text p + p { margin-top: 26px; }
  .feature-cta { position: absolute; left: 478px; top: 248px; font-size: 19.5px; }

  /* Footer */
  .site-footer {
    position: absolute; left: 0; top: 985px; width: 1200px; height: 215px;
    background: linear-gradient(180deg, var(--navy) 0%, var(--navy-deep) 100%);
    border-top: 2px solid var(--cyan-line);
    display: grid; grid-template-columns: 200px 1fr 1fr 1fr 1fr 190px;
  }
  .footer-col { border-left: 1px dashed rgba(120,150,200,.35); padding: 42px 0 0 20px; }
  .footer-col:first-child { border-left: none; padding-left: 56px; }
  .footer-nav a { display: block; font-size: 20px; color: rgba(170,190,220,.45); text-decoration: none; line-height: 1.2; }
  .follow-title { font-size: 20px; color: rgba(170,190,220,.55); }
  .follow-icons { display: flex; gap: 8px; margin-top: 14px; }
  .follow-icons span { width: 26px; height: 26px; border-radius: 3px; background: #3b78c4; }
</style>
</head>
<body>
<div class="page">

  <header class="site-header">
    <div class="brand">
      <span class="brand-mark"></span>
      <span class="brand-name">Velorast Biologics</span>
    </div>
    <nav class="main-nav">
      <a class="is-current" href="#">Home</a>
      <a href="#">Facilities</a>
      <a href="#">Team</a>
      <a href="#">Links</a>
      <a href="#">Contact</a>
    </nav>
  </header>

  <section class="hero">
    <svg class="hero-swoosh" width="1140" height="260" viewBox="0 0 1140 260">
      <path d="M0 150 C300 60 700 260 1140 120 L1140 170 C700 300 300 110 0 200 Z" fill="rgba(120,170,230,.18)"/>
      <path d="M0 60 C400 0 800 140 1140 40" stroke="rgba(160,200,240,.25)" stroke-width="3" fill="none"/>
    </svg>
    <div class="hero-photo hero-photo--left" role="img" aria-label="Photo of a scientist in a lab coat at a bench"></div>
    <div class="hero-photo hero-photo--right" role="img" aria-label="Photo of researchers reviewing lab samples"></div>
    <div class="hero-photo hero-photo--main" role="img" aria-label="Photo of a lab team working at a computer"></div>
    <div class="hero-pager"><span>1</span><span>2</span><span class="is-active">3</span><span>4</span></div>
  </section>

  <h1 class="section-bar">Welcome</h1>

  <div class="intro">
    <p>Velorast Biologics (VBL) is a Contract Manufacturing Organization (CMO) located in Bayhaven, Florida.<br>
    VBL is currently in the process of commissioning a state-of-the-art biological manufacturing facility using the Flexivane- Single Use Disposable Plastic Bags which reduces risks of cross-contamination between batches. VBL has a fully equipped Quality Control laboratory and Process Development Laboratory.</p>
    <svg class="divider-arrow" width="1010" height="10" viewBox="0 0 1010 10">
      <line x1="0" y1="5" x2="990" y2="5" stroke="var(--rule)" stroke-dasharray="3 2"/>
      <path d="M982 1 L990 5 L982 9 M994 1 L1002 5 L994 9" stroke="var(--rule)" fill="none"/>
    </svg>
  </div>

  <section class="feature">
    <div class="feature-photo" role="img" aria-label="Photo of a bright clean-room laboratory with a technician at a workstation"></div>
    <div class="feature-text">
      <p>VBL's core expertise in in plasma derived components for the human, veterinary and diagnostic market. The nature of its facility will allow to evaluate other biological based raw material for extraction and purification.</p>
      <p>Our facility is ideal for GMP components for pre-clinical, clinical and commercial launch production.</p>
    </div>
    <p class="feature-cta">For additional information, please contact us with your project.</p>
  </section>

  <footer class="site-footer">
    <div class="footer-col">
      <nav class="footer-nav">
        <a href="#">Home</a><a href="#">Facilities</a><a href="#">Team</a><a href="#">Links</a><a href="#">Contact</a>
      </nav>
    </div>
    <div class="footer-col"></div>
    <div class="footer-col"></div>
    <div class="footer-col"></div>
    <div class="footer-col"></div>
    <div class="footer-col">
      <p class="follow-title">Follow us</p>
      <div class="follow-icons"><span></span><span></span></div>
    </div>
  </footer>

</div>
</body>
</html>
```